Welcome Card

We are a property management company and I need to attach this postcard to 2 packages of microwave popcorn as a welcome gift to our new tenant.Here is the copy for the postcard (FRONT SIDE): Just "popped" in to make sure your apartment was ready for you! Enjoy your Stay.........UNITED APARTMENTSBACK SIDE: Welcome image with the words "Thank You"

Industry/Entity Type

It Company

Font styles to use
Sans Serif

```html
<!DOCTYPE html>
<html lang="en">
<head>
<meta charset="utf-8">
<title>Bramble Apartments Welcome Postcard</title>
<link href="https://fonts.googleapis.com/css2?family=Saira+Condensed:wght@500;600;700&family=Cormorant+Garamond:ital,wght@1,700&family=Open+Sans:wght@400;600&display=swap" rel="stylesheet">
<style>
  :root {
    --page: #ececec;
    --card-white: #ffffff;
    --panel-light: #fbfbfb;
    --panel-mid: #d6d6d6;
    --brand-blue: #1f63c6;
    --brand-dark: #2f2f33;
    --navy: #1b2a5c;
    --link-blue: #2b56b0;
    --rule: #333333;
    --photo-sky: #9fc47a;
    --photo-grass: #4f9a2a;
    --photo-room: #dfe3e2;
    --photo-room-warm: #c9cfc4;
  }
  * { box-sizing: border-box; margin: 0; padding: 0; }
  html, body { width: 900px; height: 1200px; overflow: hidden; }
  body { background: var(--page); position: relative; font-family: "Open Sans", sans-serif; }

  .postcard {
    position: absolute;
    left: 95px;
    width: 713px;
    height: 555px;
    background: var(--card-white);
    box-shadow: 0 6px 18px rgba(0,0,0,.25);
    overflow: hidden;
  }
  .postcard--front { top: 20px; }
  .postcard--back { top: 605px; }
  .postcard svg.card-art { position: absolute; inset: 0; }

  .name-plate {
    position: absolute;
    left: 88px; top: 370px;
    width: 314px; height: 53px;
    background: var(--brand-dark);
    border-radius: 6px;
    box-shadow: 0 4px 8px rgba(0,0,0,.35);
    display: flex; align-items: center; justify-content: center;
    white-space: nowrap;
    font-family: "Saira Condensed", sans-serif;
    font-weight: 700;
    font-size: 31px;
    line-height: 1;
    letter-spacing: 0;
    color: #f2f2f2;
    text-shadow: 0 0 2px #000;
  }
  .tagline {
    position: absolute;
    left: 55px; top: 436px;
    width: 390px;
    text-align: center;
    white-space: nowrap;
    font-family: "Saira Condensed", sans-serif;
    font-weight: 600;
    font-size: 26px;
    line-height: 31px;
    color: var(--navy);
    text-transform: uppercase;
  }
  .brand-name {
    position: absolute;
    left: 510px; top: 440px;
    width: 190px;
    text-align: center;
    font-family: "Saira Condensed", sans-serif;
    font-weight: 700;
    font-size: 28px;
    line-height: 30px;
    color: var(--navy);
  }

  .thank-you {
    position: absolute;
    left: 100px; top: 368px;
    font-family: "Cormorant Garamond", serif;
    font-style: italic;
    font-weight: 700;
    font-size: 66px;
    line-height: 64px;
    color: var(--navy);
    text-shadow: 2px 3px 4px rgba(0,0,0,.3);
  }
  .thank-you span { display: block; }
  .thank-you span + span { padding-left: 115px; }
  .web-address {
    position: absolute;
    left: 88px; top: 518px;
    font-size: 17px;
    color: var(--link-blue);
    white-space: nowrap;
  }
  .stamp-box {
    position: absolute;
    left: 581px; top: 65px;
    width: 99px; height: 99px;
    border: 2px solid var(--rule);
  }
  .address-line {
    position: absolute;
    left: 523px;
    width: 159px;
    height: 2px;
    background: var(--rule);
  }
  .address-line--1 { top: 285px; }
  .address-line--2 { top: 322px; }
  .address-line--3 { top: 361px; }
</style>
</head>
<body>

<section class="postcard postcard--front">
  <svg class="card-art" width="713" height="555" viewBox="0 0 713 555">
    <defs>
      <linearGradient id="panelFront" x1="0" y1="0" x2="1" y2="0">
        <stop offset="0" stop-color="var(--panel-mid)"/>
        <stop offset="0.5" stop-color="var(--panel-light)"/>
        <stop offset="1" stop-color="var(--panel-mid)"/>
      </linearGradient>
      <linearGradient id="housePhoto" x1="0" y1="0" x2="0" y2="1">
        <stop offset="0" stop-color="var(--photo-sky)"/>
        <stop offset="0.55" stop-color="#b7a98f"/>
        <stop offset="1" stop-color="var(--photo-grass)"/>
      </linearGradient>
    </defs>
    <rect width="713" height="555" fill="url(#panelFront)"/>
    <polygon points="0,0 713,0 713,162 572,362 0,362" fill="var(--brand-dark)"/>
    <polygon points="0,0 713,0 713,150 565,355 0,355" fill="var(--brand-blue)"/>
    <polygon points="0,0 713,0 713,138 560,348 0,348" fill="url(#housePhoto)" role="img" aria-label="Photo of a cream Victorian house with porch, green lawn and flower beds"/>
    <rect x="0" y="537" width="713" height="18" fill="var(--brand-blue)"/>
  </svg>
  <div class="name-plate">BRAMBLE APARTMENTS</div>
  <p class="tagline">Just "popped" in to make sure your<br>apartment was ready for you!<br>Enjoy your stay.........</p>
  <p class="brand-name">Bramble Apartments</p>
</section>

<section class="postcard postcard--back">
  <svg class="card-art" width="713" height="555" viewBox="0 0 713 555">
    <defs>
      <linearGradient id="panelBack" x1="0" y1="0" x2="1" y2="0">
        <stop offset="0" stop-color="var(--panel-mid)"/>
        <stop offset="0.6" stop-color="var(--panel-light)"/>
        <stop offset="1" stop-color="#c4c4c4"/>
      </linearGradient>
      <linearGradient id="roomPhoto" x1="0" y1="0" x2="1" y2="1">
        <stop offset="0" stop-color="var(--photo-room)"/>
        <stop offset="1" stop-color="var(--photo-room-warm)"/>
      </linearGradient>
    </defs>
    <rect width="448" height="555" fill="url(#panelBack)"/>
    <polygon points="0,0 448,0 448,86 250,358 0,358" fill="var(--brand-dark)"/>
    <polygon points="0,0 448,0 448,76 244,352 0,352" fill="var(--brand-blue)"/>
    <polygon points="0,0 448,0 448,64 238,345 0,345" fill="url(#roomPhoto)" role="img" aria-label="Photo of a smiling couple in a bright modern apartment"/>
    <line x1="448" y1="0" x2="448" y2="555" stroke="#e2e2e2" stroke-width="1"/>
  </svg>
  <h2 class="thank-you"><span>Thank</span><span>You</span></h2>
  <p class="web-address">www.brambleapartment.com</p>
  <div class="stamp-box"></div>
  <div class="address-line address-line--1"></div>
  <div class="address-line address-line--2"></div>
  <div class="address-line address-line--3"></div>
</section>

</body>
</html>
```